Corvant Systems Business Card

Create an appealing and elegant Business card for corvant systems. Include logo and use related colors from website, be creative. Include Business name, my name, tile, address, contacts, address, and social media contacts if possible. Logo PSD file is attached.

Bleed Area: 3.46" x 2.32"
Trim: 3.3" x 2.16"
Safe Area: 3.14" x 2.02"

Save files as vector-based PDF with outlined text and PNG.
No crop marks
CMYK color setting

Business Card Info:

Corvant Systems

Dennis Halvorsen
Owner

512 Brindlemoor Rd Unit C
Alder Cove, NR 02871
t. 1.888.555.0162
e. dennis.h@corvantsys.example
w. www.corvantsys.example

facebook. www.friendloop.example/CorvantSys
twitter. chirpline.example/corvantsys
pinterest. www.pinboard.example/corvantsys/

Target Market(s)

Business Owners and Partners

Industry/Entity Type

Business

Requirements
Must have
• Logo and related colors from website

```html
<!DOCTYPE html>
<html lang="en">
<head>
<meta charset="utf-8">
<title>Corvant Systems Business Card</title>
<link rel="stylesheet" href="https://fonts.googleapis.com/css2?family=Arimo:wght@400;700&family=Open+Sans:wght@400&display=swap">
<style>
  :root {
    --backdrop: #2e2e2e;
    --card-white: #ffffff;
    --brand-blue: #4f74a8;
    --brand-blue-shade: #4a6b9e;
    --ink: #111111;
  }
  * { margin: 0; padding: 0; box-sizing: border-box; }
  html, body {
    width: 1200px; height: 1000px; overflow: hidden;
    background: var(--backdrop);
  }
  .stage { position: relative; width: 1200px; height: 1000px; }

  .card { position: absolute; overflow: hidden; }
  .card--front {
    left: 115px; top: 119px; width: 439px; height: 750px;
    background: var(--card-white);
    font-family: "Arimo", Arial, sans-serif;
  }
  .card--back {
    left: 641px; top: 119px; width: 445px; height: 744px;
    background: var(--brand-blue);
  }

  .wordmark {
    font-family: "Open Sans", sans-serif;
    font-weight: 400;
    color: var(--ink);
    line-height: 1;
  }
  .card--front .wordmark {
    position: absolute; right: 36px; top: 78px; text-align: right;
    font-size: 46px;
  }
  .wordmark span { display: block; }
  .wordmark span + span { margin-top: 6px; }

  .decor-tower {
    position: absolute; left: 0; top: 253px; width: 112px; height: 478px;
    background: var(--brand-blue);
  }
  .front-band {
    position: absolute; left: 0; bottom: 0; width: 100%; height: 19px;
    background: var(--brand-blue);
  }

  .holder { position: absolute; right: 42px; top: 251px; text-align: right; }
  .holder__name { color: var(--brand-blue); font-size: 21px; font-weight: 400; }
  .holder__name strong { font-weight: 700; }
  .holder__title { color: var(--ink); font-size: 16px; margin-top: 4px; }

  .address {
    position: absolute; right: 45px; top: 350px; text-align: right;
    color: var(--brand-blue); font-size: 14px; line-height: 22px;
    font-style: normal;
  }

  .contact-list {
    position: absolute; right: 48px; list-style: none;
    color: var(--brand-blue); font-size: 14px;
  }
  .contact-list--direct { top: 433px; }
  .contact-list--social { top: 574px; }
  .contact-list li {
    display: flex; justify-content: flex-end; align-items: center;
    height: 26px;
  }
  .contact-list--social li { height: 29px; }
  .contact-list svg { width: 20px; height: 20px; margin-left: 9px; flex: none; }

  .decor-tower-faint {
    position: absolute; left: 124px; top: 26px; width: 182px; height: 718px;
    background: var(--brand-blue-shade);
    opacity: 0.9;
  }
  .back-band {
    position: absolute; left: 0; top: 280px; width: 100%; height: 153px;
    background: var(--card-white);
    display: flex; align-items: center; justify-content: center;
  }
  .back-band .wordmark { font-size: 48px; text-align: center; }
</style>
</head>
<body>
<main class="stage">

  <section class="card card--front" aria-label="Business card front">
    <div class="wordmark"><span>Corvant</span><span>Systems</span></div>

    <div class="decor-tower" role="img" aria-label="Large lighthouse silhouette in brand blue"></div>
    <div class="front-band"></div>

    <div class="holder">
      <p class="holder__name"><strong>Dennis</strong> Halvorsen</p>
      <p class="holder__title">Owner</p>
    </div>

    <address class="address">
      512 Brindlemoor Rd Unit C<br>
      Alder Cove, NR 02871
    </address>

    <ul class="contact-list contact-list--direct">
      <li>1.888.555.0162
        <svg viewBox="0 0 20 20" aria-hidden="true"><circle cx="10" cy="10" r="8.5" fill="none" stroke="#111" stroke-width="1.3"/><path d="M7.2 5.5l1.6 2.2-1 1.2c.6 1.3 1.6 2.3 2.9 2.9l1.2-1 2.2 1.6-.8 1.6c-3.4-.3-6.4-3.3-6.7-6.7z" fill="#111"/></svg>
      </li>
      <li>dennis.h@corvantsys.example
        <svg viewBox="0 0 20 20" aria-hidden="true"><circle cx="10" cy="10" r="8.5" fill="none" stroke="#111" stroke-width="1.3"/><text x="10" y="14" font-size="11" text-anchor="middle" font-family="Arial, sans-serif" fill="#111">@</text></svg>
      </li>
      <li>www.corvantsys.example
        <svg viewBox="0 0 20 20" aria-hidden="true"><g fill="none" stroke="#111" stroke-width="1.1"><circle cx="10" cy="10" r="7.5"/><ellipse cx="10" cy="10" rx="3.3" ry="7.5"/><path d="M2.5 10h15M4 6h12M4 14h12"/></g></svg>
      </li>
    </ul>

    <ul class="contact-list contact-list--social">
      <li>www.friendloop.example/CorvantSys
        <svg viewBox="0 0 20 20" aria-hidden="true"><circle cx="10" cy="10" r="8.5" fill="none" stroke="#111" stroke-width="1.3"/></svg>
      </li>
      <li>chirpline.example/corvantsys
        <svg viewBox="0 0 20 20" aria-hidden="true"><circle cx="10" cy="10" r="8.5" fill="none" stroke="#111" stroke-width="1.3"/></svg>
      </li>
      <li>www.pinboard.example/corvantsys/
        <svg viewBox="0 0 20 20" aria-hidden="true"><circle cx="10" cy="10" r="8.5" fill="none" stroke="#111" stroke-width="1.3"/></svg>
      </li>
    </ul>
  </section>

  <section class="card card--back" aria-label="Business card back">
    <div class="decor-tower-faint" role="img" aria-label="Faint lighthouse silhouette in a darker blue"></div>
    <div class="back-band">
      <div class="wordmark"><span>Corvant</span><span>Systems</span></div>
    </div>
  </section>

</main>
</body>
</html>
```